Label design for Japanese healthy drink

We need new label design to give our product a new look. This is Amazake, traditional Japanese drink made out of fermented rice. This is nutrition packed drink and target audience is health conscious people. We want something simple and healthy. The attached photo is current label (for the size reference only) and food pouch the label will be attached. Please don't use anything on the label in the picture.

Target Market(s)

health conscious people (30s - 50s)

Requirements
Must have
• "Amazake"
Should not have
• too much color, picture of rice or sake

```html
<!DOCTYPE html>
<html lang="en">
<head>
<meta charset="utf-8">
<title>Amazake Label</title>
<link rel="stylesheet" href="https://fonts.googleapis.com/css2?family=Familjen+Grotesk:wght@400;500;700&family=Noto+Sans+JP:wght@400&display=swap">
<style>
  :root {
    --backdrop: #f1f0f3;
    --label-dark: #231b22;
    --wave-tone: #5a2444;
    --magenta: #bd1564;
    --white: #ffffff;
    --ink: #1d1a1c;
  }
  * { margin: 0; padding: 0; box-sizing: border-box; }
  html, body {
    width: 779px;
    height: 1200px;
    overflow: hidden;
    background: var(--backdrop);
  }
  .label {
    position: absolute;
    left: 39px;
    top: 250px;
    width: 700px;
    height: 700px;
  }
  .label__pattern {
    position: absolute;
    inset: 0;
    background: radial-gradient(circle at 50% 50%, var(--wave-tone) 0%, var(--label-dark) 75%);
  }
  .label__panel {
    position: absolute;
    left: 120px;
    top: 120px;
    width: 460px;
    height: 460px;
    background: var(--white);
    border-radius: 24px;
    text-align: center;
    font-family: "Familjen Grotesk", sans-serif;
    color: var(--ink);
  }
  .kanji {
    position: absolute;
    top: 62px;
    width: 100%;
    font-family: "Noto Sans JP", sans-serif;
    font-size: 30px;
    line-height: 1;
  }
  .product-name {
    position: absolute;
    top: 130px;
    width: 100%;
    font-weight: 700;
    font-size: 84px;
    line-height: 1;
    letter-spacing: -2px;
    color: var(--magenta);
  }
  .description {
    position: absolute;
    top: 262px;
    width: 100%;
    font-weight: 500;
    font-size: 19px;
    line-height: 1.1;
    letter-spacing: -0.3px;
  }
  .divider {
    position: absolute;
    top: 348px;
    left: 220px;
    width: 20px;
    height: 7px;
    background: var(--magenta);
  }
  .net-weight {
    position: absolute;
    top: 370px;
    width: 100%;
    font-size: 17px;
    line-height: 1;
  }
</style>
</head>
<body>
  <div class="label">
    <div class="label__pattern" role="img" aria-label="Dark background with fine magenta wavy line pattern"></div>
    <div class="label__panel">
      <div class="kanji" lang="ja">甘酒</div>
      <h1 class="product-name">Amazake</h1>
      <p class="description">Traditional Japanese<br>drink made out of<br>fermented rice</p>
      <div class="divider"></div>
      <p class="net-weight">150 g</p>
    </div>
  </div>
</body>
</html>
```